Veltarum

Standard Business Card design.
Sample two-sided design uploaded. White front, Black back.
Would like white shield to be on all black background side.
Willing to look at a couple creative designs, but nothing crazy.
Preference for a classic, confident, strong design.

```html
<!DOCTYPE html>
<html lang="en">
<head>
<meta charset="utf-8">
<title>Veltarum — Business Card</title>
<link href="https://fonts.googleapis.com/css2?family=Poppins:wght@300;400;600;700&display=swap" rel="stylesheet">
<style>
  :root {
    --backdrop: #e9e7e3;
    --card-white: #ffffff;
    --card-black: #0b0c0e;
    --ink: #111214;
    --ink-soft: #2b2c2f;
    --paper-text: #f4f4f4;
  }
  * { box-sizing: border-box; margin: 0; padding: 0; }
  html, body {
    width: 1200px; height: 892px; overflow: hidden;
    background: var(--backdrop);
    font-family: "Poppins", sans-serif;
  }
  .sheet {
    width: 1200px; height: 892px;
    display: flex; flex-direction: column; align-items: center; justify-content: center;
    gap: 56px;
  }
  .card {
    width: 620px; height: 354px;
    position: relative;
    box-shadow: 0 6px 18px rgba(0,0,0,0.14);
  }
  /* Front */
  .card--front { background: var(--card-white); color: var(--ink); }
  .front__brand {
    position: absolute; left: 48px; top: 60px;
    display: flex; align-items: center; gap: 12px;
    font-weight: 600; font-size: 28px; letter-spacing: 3px; text-transform: uppercase;
    color: var(--ink);
  }
  .front__brand-square { width: 14px; height: 14px; background: var(--ink); }
  .front__identity {
    position: absolute; left: 300px; top: 108px;
  }
  .identity__first { font-weight: 700; font-size: 21px; letter-spacing: 0.5px; line-height: 1.1; }
  .identity__last { font-weight: 300; font-size: 21px; line-height: 1.2; text-transform: uppercase; }
  .identity__role { font-weight: 400; font-size: 10px; letter-spacing: 6px; margin-top: 6px; text-transform: uppercase; color: var(--ink-soft); }
  .front__rule {
    position: absolute; left: 300px; right: 44px; top: 206px;
    height: 3px; background: var(--ink);
  }
  .front__contacts {
    position: absolute; left: 48px; right: 44px; top: 228px;
    display: flex; justify-content: space-between;
    font-size: 10.5px; font-weight: 400; text-transform: uppercase; color: var(--ink);
  }
  .contact { display: flex; align-items: center; gap: 5px; }
  .contact svg { width: 10px; height: 10px; fill: var(--ink); }
  .front__address {
    position: absolute; right: 44px; bottom: 40px;
    text-align: right; font-size: 12px; letter-spacing: 3px; line-height: 1.5; text-transform: uppercase;
  }
  /* Back */
  .card--back {
    background: var(--card-black); color: var(--paper-text);
    display: flex; flex-direction: column; align-items: center; justify-content: center;
    gap: 22px;
  }
  .back__mark-square { width: 64px; height: 64px; background: var(--paper-text); }
  .back__brand {
    font-weight: 600; font-size: 48px; line-height: 1; letter-spacing: 8px; text-transform: uppercase;
    color: var(--paper-text);
    padding-left: 8px;
  }
</style>
</head>
<body>
<main class="sheet">
  <section class="card card--front" aria-label="Card front">
    <div class="front__brand"><span class="front__brand-square"></span>Veltarum</div>
    <div class="front__identity">
      <p class="identity__first">ADRIAN</p>
      <p class="identity__last">Mathis Laurent</p>
      <p class="identity__role">Designation</p>
    </div>
    <div class="front__rule"></div>
    <div class="front__contacts">
      <span class="contact">
        <svg viewBox="0 0 10 10"><circle cx="5" cy="5" r="4.3" fill="none" stroke="#111214" stroke-width="1"/><path d="M0.8 5h8.4M5 0.8v8.4" stroke="#111214" stroke-width="0.8"/></svg>
        www.yourwebsite.com
      </span>
      <span class="contact">
        <svg viewBox="0 0 10 10"><path d="M0 4.5 10 0 6 10 4.6 5.6Z"/></svg>
        info@yourmailid.com
      </span>
      <span class="contact">
        <svg viewBox="0 0 10 10"><path d="M2 0.5 3.8 2.6 2.9 3.9Q4 6.2 6.1 7.1L7.4 6.2 9.5 8 8.4 9.5Q1 8.5 0.5 1.6Z"/></svg>
        +00 123 4567 89
      </span>
    </div>
    <div class="front__address">1234 Your Streets Location<br>Country</div>
  </section>

  <section class="card card--back" aria-label="Card back">
    <span class="back__mark-square" aria-hidden="true"></span>
    <div class="back__brand">Veltarum</div>
  </section>
</main>
</body>
</html>
```